A4 Flyer to introduce new line of ice cream cakes and dessert in a bakery shop

[The flyer should have written:]

Welcome to our new line of ice-cream desserts.

As everything else, all hand-made in our kitchen only with natural ingredients.

Try our new....

[then three sections with the following products]

* Ice-cream cakes
* Ice-creams
* Cookie ice-creams

Target Market(s)

Families

Industry/Entity Type

Shop

Font styles to use
Other font styles liked:
• Futura

Requirements
Must have
• Please include our logo on the flyer (see file attached)

```html
<!DOCTYPE html>
<html lang="en">
<head>
<meta charset="UTF-8">
<title>Gelatella – New Ice-Cream Desserts</title>
<link href="https://fonts.googleapis.com/css2?family=Jost:wght@400;500;600;700&display=swap" rel="stylesheet">
<style>
  :root {
    --brown: #4a2b1d;
    --gold: #b98b2c;
    --ink: #262626;
    --body: #3d3d3d;
    --paper: #ffffff;
    --cream: #e9dcc6;
    --cocoa: #7a5236;
  }
  * { box-sizing: border-box; margin: 0; padding: 0; }
  html, body { width: 849px; height: 1200px; overflow: hidden; background: var(--paper); }
  .flyer {
    position: relative;
    width: 849px;
    height: 1200px;
    background: var(--gold);
    font-family: 'Jost', 'Futura', sans-serif;
  }
  .masthead {
    position: absolute; left: 0; top: 0; width: 849px; height: 100px;
    background: var(--brown);
    display: flex; align-items: center; justify-content: center; gap: 10px;
  }
  .brand-dot { width: 14px; height: 14px; border-radius: 50%; background: var(--gold); }
  .brand-name { color: var(--gold); font-size: 30px; font-weight: 500; letter-spacing: 1px; }
  .panel {
    position: absolute; left: 14px; top: 100px; width: 821px; height: 1020px;
    background: var(--paper);
  }
  .photo { position: absolute; top: 20px; height: 305px; }
  .photo-bars { left: 9px; width: 398px;
    background: linear-gradient(90deg, #6b4128 0%, #d9c3a0 30%, #4a2a1a 55%, #e6d6bc 80%, #8a5a38 100%); }
  .photo-pops { left: 426px; width: 390px;
    background: radial-gradient(circle at 50% 45%, #b48a5e 0%, #d8c2a4 45%, #eeeeee 80%); }
  .welcome {
    position: absolute; left: 36px; top: 390px;
    color: var(--gold); font-size: 104px; font-weight: 700; line-height: 1;
  }
  .intro {
    position: absolute; left: 36px; top: 505px;
    color: var(--ink); font-size: 35px; font-weight: 600; line-height: 1.2;
  }
  .promise {
    position: absolute; left: 36px; top: 560px; width: 760px;
    color: var(--body); font-size: 33px; font-weight: 400; line-height: 1.25;
  }
  .try {
    position: absolute; left: 36px; top: 700px;
    color: var(--ink); font-size: 40px; font-weight: 600;
  }
  .products { position: absolute; left: 0; top: 790px; width: 821px; height: 200px; }
  .product { position: absolute; top: 0; width: 250px; text-align: center; }
  .product:nth-child(1) { left: 30px; }
  .product:nth-child(2) { left: 265px; }
  .product:nth-child(3) { left: 520px; }
  .product-art { width: 130px; height: 130px; margin: 0 auto; border-radius: 50%;
    background: radial-gradient(circle, var(--cocoa) 0%, var(--cream) 60%, var(--paper) 75%); }
  .product-art.cake { background: radial-gradient(circle at 50% 40%, #e07aa0 0%, #f3c3d4 40%, #c59a5a 60%, var(--paper) 75%); }
  .product-art.cone { background: radial-gradient(circle at 50% 35%, #f5ecd9 0%, #e6b96d 45%, var(--paper) 72%); }
  .product-name { margin-top: 30px; color: var(--ink); font-size: 28px; font-weight: 600; }
</style>
</head>
<body>
<div class="flyer">
  <header class="masthead">
    <span class="brand-dot"></span>
    <span class="brand-name">gelatella</span>
  </header>
  <main class="panel">
    <div class="photo photo-bars" role="img" aria-label="Row of chocolate-dipped ice-cream sandwich bars with nut toppings"></div>
    <div class="photo photo-pops" role="img" aria-label="Tray of ice-cream pops on sticks coated in chocolate, nuts and pistachio"></div>
    <h1 class="welcome">Welcome</h1>
    <p class="intro">to our new line of ice-cream desserts.</p>
    <p class="promise">As everything else, all hand-made in our kitchen only with natural ingredients.</p>
    <p class="try">Try our new....</p>
    <section class="products">
      <div class="product">
        <div class="product-art cake" role="img" aria-label="Ice-cream cupcake illustration"></div>
        <p class="product-name">Ice-cream cakes</p>
      </div>
      <div class="product">
        <div class="product-art" role="img" aria-label="Chocolate ice-cream bar illustration"></div>
        <p class="product-name">Ice-creams</p>
      </div>
      <div class="product">
        <div class="product-art cone" role="img" aria-label="Ice-cream cone with cherry illustration"></div>
        <p class="product-name">Cookie ice-creams</p>
      </div>
    </section>
  </main>
</div>
</body>
</html>
```